Disability Travel Company needs a brochure for their holidays

We need a brochure designed with the details of our holidays for people with disabilities.
It needs to be in a PDF format that can be uploaded onto our website. Should not be more than 2MB in size. Needs to also be printed onto A4 paper. We will not be having it professionally printed.
No bigger than four A4 pages.

We need to be able to amend the file ourselves using Adobe Acrobat.

```html
<!DOCTYPE html>
<html lang="en">
<head>
<meta charset="utf-8">
<title>Brightway Journeys – Holiday Program Brochure</title>
<link rel="stylesheet" href="https://fonts.googleapis.com/css2?family=Oswald:wght@400;500;600&family=Open+Sans:wght@400;600;700&display=swap">
<style>
:root{
  --sheet:#ffffff;
  --page:#484848;
  --orange:#f7941d;
  --green:#00a651;
  --cream:#fdf4d6;
  --butter:#fbe3a2;
  --title:#f4e29c;
  --ink:#333333;
  --white:#ffffff;
  --label-red:#e53935;
}
*{margin:0;padding:0;box-sizing:border-box}
html,body{width:1200px;height:897px;overflow:hidden;background:var(--sheet)}
body{position:relative;font-family:"Open Sans",Arial,sans-serif;color:var(--white)}
.sheet-frame{position:absolute;left:2px;top:2px;width:1196px;height:893px;border:1px solid #cfcfcf}
.option-label{position:absolute;top:12px;left:0;width:1200px;text-align:center;color:var(--label-red);font-size:20px;font-family:Arial,sans-serif}
.page-label{position:absolute;top:856px;font-size:19px;color:var(--ink);font-family:Arial,sans-serif}
.page{position:absolute;top:34px;height:819px;background:var(--page);overflow:hidden}
.page--back{left:34px;width:566px}
.page--cover{left:604px;width:588px}
.band-green{position:absolute;left:0;right:0;top:790px;height:8px;background:var(--green)}
.band-orange{position:absolute;left:0;right:0;top:801px;height:18px;background:var(--orange)}

.snapshot{position:absolute;background:var(--orange);padding:7px;box-shadow:1px 2px 3px rgba(0,0,0,.35)}
.snapshot .photo{width:100%;height:100%}
.photo--beach{background:linear-gradient(180deg,#6fa8dc 0%,#b7d3ea 45%,#d8c08e 70%,#a88657 100%)}
.photo--monument{background:linear-gradient(180deg,#9ec6e8 0%,#d9dde0 55%,#b9a68a 100%)}
.photo--carriage{background:linear-gradient(180deg,#8fb6d8 0%,#6f8a5a 50%,#5a4a3a 100%)}
.photo--water{background:linear-gradient(180deg,#7fbcd6 0%,#3aa0b8 55%,#2a7f8c 100%)}
.photo--group{background:linear-gradient(160deg,#b9a48c 0%,#8a7565 50%,#4f5a70 100%)}
.avatar{position:absolute;left:329px;width:32px;height:38px;background:linear-gradient(180deg,#d9d9d9,#8c8c8c)}

.section-title{position:absolute;left:31px;top:61px;font-family:Oswald,sans-serif;font-weight:500;font-size:13px;line-height:16px;color:var(--orange);letter-spacing:.2px}
.quote{position:absolute;left:31px;width:355px;font-size:8.3px;line-height:11.3px;color:var(--white)}
.quote-author{position:absolute;left:31px;font-size:8.3px;font-weight:700;color:var(--orange)}
.quote-author span{font-weight:400}
.back-cta{position:absolute;left:0;width:566px;top:654px;text-align:center;font-size:12.5px;color:var(--white)}
.brand{font-family:Oswald,sans-serif;font-weight:600;color:var(--orange);text-transform:uppercase;letter-spacing:.5px;line-height:1.05;display:flex;align-items:center;gap:8px}
.brand-mark{width:14px;height:14px;border-radius:50%;background:var(--orange);flex:none}
.back-brand{position:absolute;top:694px;left:0;width:566px;justify-content:center;font-size:18px}
.contact{position:absolute;top:762px;left:0;width:566px;text-align:center;font-family:Oswald,sans-serif;font-weight:500;font-size:12px;letter-spacing:.2px}

.cover-brand{position:absolute;top:56px;left:0;width:588px;justify-content:center;font-size:20px}
.cover-title{position:absolute;top:117px;left:0;width:588px;text-align:center;font-family:Oswald,sans-serif;font-weight:600;font-size:31px;color:var(--title);letter-spacing:.5px}
.intro{position:absolute;top:326px;left:0;width:588px;text-align:center;font-size:10.3px;line-height:19.5px;font-weight:700}
.intro svg{vertical-align:-2px}
.categories{position:absolute;left:33px;top:392px;width:501px;border-collapse:collapse;table-layout:fixed}
.categories th{height:26px;font-family:Oswald,sans-serif;font-weight:500;font-size:10px;color:var(--white);text-align:center;border:1px solid var(--green)}
.categories td{vertical-align:top;padding:6px 4px;font-size:7.4px;line-height:10.2px;color:var(--ink);border:1px solid var(--green);height:240px}
.categories td p{margin-bottom:10px}
.cat-i{background:var(--green)}
.cat-g{background:var(--orange)}
.cat-e{background:var(--green)}
.cat-p{background:var(--orange)}
.body-i{background:var(--cream)}
.body-g{background:var(--butter)}
.body-e{background:var(--white)}
.body-p{background:var(--butter)}
.notes{position:absolute;left:33px;top:674px;width:520px;font-size:6px;line-height:8.6px;font-weight:700;color:var(--white)}
.notes h4{color:var(--orange);font-size:6px;font-weight:700;margin-top:7px}
.notes h4:first-child{margin-top:0}
</style>
</head>
<body>
<div class="sheet-frame"></div>
<div class="option-label">Option_1</div>

<section class="page page--back">
  <h2 class="section-title">Customer Stories | TESTIMONIALS</h2>
  <svg width="566" height="819" style="position:absolute;left:0;top:0" aria-hidden="true">
    <polyline points="240,69 394,69 394,600 274,600" fill="none" stroke="#f7941d" stroke-width="1.2"/>
    <polyline points="34,720 34,792 531,792 531,720 360,720" fill="none" stroke="#d9d9d9" stroke-width="1"/>
    <line x1="34" y1="720" x2="170" y2="720" stroke="#d9d9d9" stroke-width="1"/>
  </svg>

  <p class="quote" style="top:83px">We would like to thank you for a very pleasant itinerary (Senegal –The Gambia – Guinea Bissau 16 days) and a fantastic driver and guide. We had a great time together getting the ultimate experience of our Holiday.</p>
  <p class="quote-author" style="top:130px">Per Halvorsrud, Norway</p>
  <div class="avatar" style="top:118px" role="img" aria-label="Portrait of the traveller"></div>

  <p class="quote" style="top:176px">Thank you for your mail and concern. Everything went fine during the trip in Cote D'Ivoire. We had a wonderful time in a wonderful country.</p>
  <p class="quote-author" style="top:209px">Nikolaos Theriotis and Petros Kalamaris, Greece</p>
  <div class="avatar" style="top:209px" role="img" aria-label="Portrait of the traveller"></div>

  <p class="quote" style="top:262px">Our trip was amazing! We really appreciated all the hard work you did to make this trip enjoyable!</p>
  <p class="quote-author" style="top:298px">M. Harlan, Northfield Academy</p>
  <div class="avatar" style="top:291px" role="img" aria-label="Portrait of the traveller"></div>

  <p class="quote" style="top:332px">Our trip was amazing! We really appreciated all the hard work you did to make this trip enjoyable! Please pass along that we were EXTREMELY pleased with Horizon Tours, especially our tour guide, Mr. Ekow Tandoh!"</p>
  <p class="quote" style="top:389px">Thanks,</p>
  <p class="quote-author" style="top:411px">M. Harlan, Northfield Flight Academy | Colorado, USA</p>
  <div class="avatar" style="top:385px" role="img" aria-label="Portrait of the traveller"></div>

  <p class="quote" style="top:469px">Dear Mariam Sadio,</p>
  <p class="quote" style="top:494px">I have now returned from my trip to West Africa and want to thank you for my experiences in Burkina Faso and Mali. The high points were the feeding of live chickens to the sacred crocodiles in Burkina. I would like to return to this area in the future.</p>
  <p class="quote" style="top:534px">Best regards,</p>
  <p class="quote-author" style="top:554px">Larry Wendell | <span>New York, USA</span></p>
  <div class="avatar" style="top:522px" role="img" aria-label="Portrait of the traveller"></div>

  <div class="snapshot" style="left:412px;top:77px;width:121px;height:106px;transform:rotate(5deg)"><div class="photo photo--beach" role="img" aria-label="Travellers riding camels on a beach"></div></div>
  <div class="snapshot" style="left:433px;top:203px;width:86px;height:122px;transform:rotate(-8deg)"><div class="photo photo--monument" role="img" aria-label="Family posing beside a large monument"></div></div>
  <div class="snapshot" style="left:411px;top:343px;width:123px;height:103px;transform:rotate(5deg)"><div class="photo photo--carriage" role="img" aria-label="Horse-drawn carriage ride under pine trees"></div></div>
  <div class="snapshot" style="left:411px;top:514px;width:120px;height:109px;transform:rotate(10deg)"><div class="photo photo--water" role="img" aria-label="Kayaking in clear turquoise water"></div></div>

  <p class="back-cta">First determine which category best suits you – if unsure contact us to discuss.</p>
  <div class="brand back-brand"><span class="brand-mark"></span><span style="background:var(--page);padding:0 4px">Brightway Journeys</span></div>
  <p class="contact">Telephone: (Int) + 67 23 55010 | Australia 1800 555 010 | Email: hello@brightwayjourneys.org</p>
  <div class="band-green"></div>
  <div class="band-orange"></div>
</section>

<section class="page page--cover">
  <div class="brand cover-brand"><span class="brand-mark"></span><span>Brightway Journeys</span></div>
  <svg width="588" height="819" style="position:absolute;left:0;top:0" aria-hidden="true">
    <polyline points="40,207 40,138 99,138" fill="none" stroke="#d9d9d9" stroke-width="1"/>
    <polyline points="460,138 529,138 529,207" fill="none" stroke="#d9d9d9" stroke-width="1"/>
  </svg>
  <h1 class="cover-title">HOLIDAY PROGRAM 2014</h1>

  <div class="snapshot" style="left:71px;top:194px;width:131px;height:103px;transform:rotate(-4deg)"><div class="photo photo--group" role="img" aria-label="Travellers sharing a happy moment"></div></div>
  <div class="snapshot" style="left:190px;top:175px;width:92px;height:134px;transform:rotate(12deg)"><div class="photo photo--group" role="img" aria-label="Group of friends on holiday"></div></div>
  <div class="snapshot" style="left:282px;top:189px;width:108px;height:103px;transform:rotate(-3deg)"><div class="photo photo--group" role="img" aria-label="Guests smiling together indoors"></div></div>
  <div class="snapshot" style="left:379px;top:183px;width:97px;height:114px;transform:rotate(8deg)"><div class="photo photo--group" role="img" aria-label="Guests enjoying an outing"></div></div>
  <div class="snapshot" style="left:447px;top:183px;width:92px;height:103px;transform:rotate(-5deg)"><div class="photo photo--group" role="img" aria-label="Traveller with a companion on tour"></div></div>

  <div class="intro">
    Costs do not include flights within Australia. This symbol
    <svg width="12" height="12" viewBox="0 0 24 24" aria-label="plane"><path d="M21 16v-2l-8-5V3.5a1.5 1.5 0 0 0-3 0V9l-8 5v2l8-2.5V19l-2 1.5V22l3.5-1 3.5 1v-1.5L13 19v-5.5z" fill="#ffffff"/></svg>
    indicates inclusive of International flights.<br>
    INFORMATION SHEETS contain full details – please email or telephone to request.<br>
    First determine which category best suits you – if unsure contact us to discuss.
  </div>

  <table class="categories">
    <colgroup><col style="width:97px"><col style="width:152px"><col style="width:143px"><col style="width:109px"></colgroup>
    <thead>
      <tr>
        <th class="cat-i">“I” &nbsp;INDEPENDENT</th>
        <th class="cat-g">“G” GENERAL</th>
        <th class="cat-e">“E” EXTRA ASSIST</th>
        <th class="cat-p">“P” PHYSICAL</th>
      </tr>
    </thead>
    <tbody>
      <tr>
        <td class="body-i">
          <p>Support Ratio 1-to-5</p>
          <p>Mild intellectual/learning disability.</p>
          <p>Minimal assistance with daily living. Prompt only.</p>
          <p>Good cognitive, communication and social skills.</p>
          <p>Good mobility.</p>
          <p>Meet Independent Travel Criteria for flights within Australia.</p>
        </td>
        <td class="body-g">
          <p>Support Ratio 1-to-3½</p>
          <p>All General category holidays are available to guests in the Independent category.</p>
          <p>Mild intellectual/learning disability.</p>
          <p>Assistance with daily living. minimal personal care-prompt, supervise, assist with hair wash, tying laces, etc. Independent toileting.</p>
          <p>Reasonable communication skills, sociable, no significant mobility challenges.</p>
        </td>
        <td class="body-e">
          <p>Support Ratio 1-to-2</p>
          <p>Mild to Moderate intellectual disability.</p>
          <p>Full assistance with daily living, including personal care support</p>
          <p>Reasonable communication skills – able to appropriately join in a social setting.</p>
          <p>Extra assistance with meals, complex medication or health concerns.</p>
          <p>Wheelchair users must be able to weight-bear to transfer with assistance to a bus and shower chair</p>
        </td>
        <td class="body-p">
          <p>Support Ratio &nbsp;as needed</p>
          <p>No Intellectual Disability</p>
          <p>Designed for guests with:</p>
          <p>Mobility challenges<br>Sensory Impairment</p>
          <p>Assistance may be required with personal care, diet, or other health concerns.</p>
        </td>
      </tr>
    </tbody>
  </table>

  <div class="notes">
    <h4>MOBILITY</h4>
    <p>Guests requiring assistance with mobility may access some ‘I’ and ‘G’ holidays.<br>Applications are considered on an individual basis and according to activities.</p>
    <h4>NO INTELLECTUAL DISABILITY?</h4>
    <p>Guests with sensory impairments, mobility challenges or other support needs but are otherwise high functioning cognitively are advised to choose “P” and ‘I’ category holidays, or discuss an Individual Holiday plan with us, where we provide support and/or travel companions.</p>
    <h4>We are unable to provide support for:</h4>
    <p>1. Severe Intellectual Disability<br>2. Challenging, Anti-Social, Violent or Aggressive Behaviours</p>
  </div>

  <div class="band-green"></div>
  <div class="band-orange"></div>
</section>

<p class="page-label" style="left:247px">Back page 4</p>
<p class="page-label" style="left:815px">Cover page 1</p>
</body>
</html>
```